Need a Poster Design A3 for our Cricket Competition

We need a poster design for our upcoming T20 cricket competition Coastal Batting Series (CBS).

it should say like this:

Lindqvist Real Estate (logo supplied)
proudly presents

Coastal Batting Series (logo supplied)

its a T20 cricket competition

starting 1st April 2018
Registrations Closing : 18th March

prizes worth $5000 to be won

for Registration contact: 0409318827 / 0408261395 and our Facebook page address..see last time's poster

and then sponsors
Updates

Hello.. We will be closing the contest earlier by 5 days so we need to get the design by Tuesday 13th Feb .. Thanks

Industry/Entity Type

Real Estate

Colors

Designer to choose colors to be used in the design.

Requirements
Must have
• emphasis on our main sponsor Lindqvist Real Estate & our competition logo

```html
<!DOCTYPE html>
<html lang="en">
<head>
<meta charset="utf-8">
<title>Coastal Batting Series – T20 Poster</title>
<link rel="stylesheet" href="https://fonts.googleapis.com/css2?family=Montserrat:wght@500;600;700;800;900&display=swap">
<style>
  :root{
    --page:#ffffff;
    --navy:#25306e;
    --sky-orange:#e8742a;
    --sky-dark:#3a1c10;
    --red:#d2202a;
    --grass:#2f6b2a;
    --grass-dark:#1d4a1c;
    --white:#ffffff;
    --ink:#2a2a2a;
    --orange:#e8541e;
    --gold:#a67a1e;
  }
  *{margin:0;padding:0;box-sizing:border-box}
  html,body{width:957px;height:1200px;overflow:hidden;background:var(--page)}
  body{font-family:"Montserrat",Arial,sans-serif;position:relative}
  .poster{position:absolute;left:112px;top:47px;width:715px;height:1104px;overflow:hidden;background:var(--grass-dark)}
  .stadium{position:absolute;left:0;top:0;width:715px;height:720px;
    background:
      radial-gradient(ellipse at 50% 30%,rgba(255,214,140,.55),rgba(255,140,60,0) 60%),
      linear-gradient(180deg,var(--sky-dark) 0%,#8a3514 14%,var(--sky-orange) 32%,#f19a4a 45%,#6a3a26 68%,#2a2430 88%,#1f2a30 100%)}
  .grass{position:absolute;left:0;top:720px;width:715px;height:384px;
    background:linear-gradient(180deg,#3d7d32 0%,var(--grass) 30%,var(--grass-dark) 100%)}

  .host{position:absolute;top:37px;left:0;width:100%;text-align:center;color:var(--white)}
  .host-mark{display:inline-block;width:22px;height:22px;background:var(--white);margin-bottom:10px}
  .host-name{font-weight:600;font-size:24px;letter-spacing:4px;line-height:1.2}
  .host-sub{font-weight:500;font-size:8px;letter-spacing:3px;margin-top:4px}

  .presents{position:absolute;top:176px;left:0;width:100%;text-align:center;
    color:var(--navy);font-weight:800;font-size:27px;letter-spacing:1px}

  .league-art{position:absolute;left:128px;top:222px;width:200px;height:208px;border-radius:18px;
    background:linear-gradient(135deg,rgba(255,255,255,.92),rgba(236,200,200,.9) 55%,rgba(210,32,42,.55))}
  .league-mark{position:absolute;left:320px;top:222px;width:300px;height:170px;background:var(--white);
    border-radius:8px;display:flex;align-items:center;justify-content:center;
    color:var(--navy);font-weight:900;font-size:118px;letter-spacing:-2px}
  .league-name{position:absolute;left:135px;top:394px;width:482px;height:46px;background:var(--white);border-radius:4px;
    display:flex;align-items:center;justify-content:center;color:var(--navy);font-weight:800;font-size:29px;letter-spacing:2px;text-transform:uppercase}

  .date-band{position:absolute;left:80px;top:446px;width:555px;height:51px}
  .date-text{position:absolute;left:80px;top:446px;width:555px;height:51px;display:flex;align-items:center;justify-content:center;
    color:var(--white);font-size:35px;font-weight:500;letter-spacing:-.5px;white-space:nowrap}
  .date-text strong{font-weight:900;margin:0 9px}

  .t20-art{position:absolute;left:200px;top:510px;width:300px;height:140px;border-radius:50%;
    background:radial-gradient(ellipse at 50% 50%,rgba(210,32,42,.9) 0%,rgba(210,32,42,.55) 55%,rgba(210,32,42,0) 72%)}
  .side-art{position:absolute;top:430px;width:130px;height:280px;
    background:radial-gradient(ellipse at 50% 50%,rgba(240,190,120,.45),rgba(240,190,120,0) 70%)}
  .side-art--left{left:0}
  .side-art--right{right:0}

  .prize{position:absolute;left:232px;top:662px;display:flex;align-items:center;color:var(--white)}
  .prize-win{font-weight:900;font-size:54px;letter-spacing:-3px;line-height:1}
  .prize-amount{margin-left:8px;line-height:1}
  .prize-amount small{display:block;font-weight:600;font-size:14px}
  .prize-amount b{display:block;font-weight:900;font-size:38px;letter-spacing:-1px}

  .thanks{position:absolute;top:757px;left:0;width:100%;text-align:center;color:var(--white);
    font-weight:800;font-size:20px;letter-spacing:-.3px}

  .sponsors{position:absolute;left:24px;top:785px;width:664px;height:184px;background:var(--white);border-radius:14px;
    display:grid;grid-template-columns:repeat(7,1fr);grid-template-rows:repeat(3,1fr);align-items:center;column-gap:8px;padding:18px 14px}
  .sponsor{display:flex;align-items:center;justify-content:center;gap:5px;text-align:center;
    font-weight:700;font-size:10px;line-height:1.15}
  .sponsor i{display:block;width:9px;height:9px;flex:none}
  .sponsor i.round{border-radius:50%}
  .c-orange{color:var(--orange)}.c-blue{color:var(--navy)}.c-red{color:var(--red)}.c-ink{color:var(--ink)}.c-gold{color:var(--gold)}

  .register{position:absolute;top:990px;left:0;width:100%;text-align:center;color:var(--white)}
  .register-title{font-weight:800;font-size:20px}
  .register-phones{font-weight:800;font-size:26px;margin-top:10px;letter-spacing:.5px}
  .register-close{font-weight:600;font-size:15px;margin-top:10px}
</style>
</head>
<body>
<main class="poster">
  <div class="stadium" role="img" aria-label="Floodlit cricket stadium at dusk with glowing orange sky"></div>
  <div class="grass" role="img" aria-label="Green cricket pitch grass"></div>

  <header class="host">
    <span class="host-mark"></span>
    <div class="host-name">LINDQVIST</div>
    <div class="host-sub">REAL ESTATE</div>
  </header>
  <p class="presents">PROUDLY PRESENTS</p>

  <div class="league-art" role="img" aria-label="Competition emblem illustration with cricket ball and batsman"></div>
  <div class="league-mark">CBS</div>
  <div class="league-name">Coastal Batting Series</div>

  <svg class="date-band" viewBox="0 0 555 51" aria-hidden="true">
    <polygon points="22,0 555,0 533,51 0,51" fill="var(--navy)"/>
  </svg>
  <p class="date-text">STARTING <strong>1ST APRIL</strong> 2018</p>

  <div class="t20-art" role="img" aria-label="T20 emblem illustration with helmet, bat, stumps and ball on red paint splash"></div>
  <div class="side-art side-art--left" role="img" aria-label="Illustration of a cricket bat"></div>
  <div class="side-art side-art--right" role="img" aria-label="Illustration of cricket stumps with flying bails"></div>

  <div class="prize">
    <span class="prize-win">WIN</span>
    <span class="prize-amount"><small>PRIZES WORTH</small><b>$5000</b></span>
  </div>

  <p class="thanks">THANKS TO ALL OUR SPONSORS AND SUPPORTERS</p>

  <section class="sponsors" aria-label="Sponsors">
    <div class="sponsor c-orange">Crest Realty</div>
    <div class="sponsor c-blue"><i style="background:var(--orange)"></i>Brightfield Finance</div>
    <div class="sponsor c-blue">Harbourline Services</div>
    <div class="sponsor c-blue"><i class="round" style="background:var(--navy)"></i>Keystone Care</div>
    <div class="sponsor c-ink"><i style="background:#111"></i>Northway Freight</div>
    <div class="sponsor c-ink">Northway Freight</div>
    <div class="sponsor c-ink">Terra Cotton Co</div>

    <div class="sponsor c-blue">Lumen Learning Hub</div>
    <div class="sponsor c-blue"><i style="background:var(--navy)"></i>Allday Truck Care</div>
    <div class="sponsor c-red"><i class="round" style="background:var(--red)"></i>Greenleaf Grocers</div>
    <div class="sponsor c-gold">Welcome Hall</div>
    <div class="sponsor c-ink">Ravel Family Trust</div>
    <div class="sponsor c-red"><i style="background:var(--red)"></i>Marlow Group</div>
    <div class="sponsor c-gold">Honeycomb Sweets</div>

    <div class="sponsor c-red">Swiftline Express</div>
    <div class="sponsor c-ink">Orbit TV</div>
    <div class="sponsor c-orange"><i class="round" style="background:var(--orange)"></i>Citrus Seven</div>
    <div class="sponsor c-blue">Pizza Corner Epping</div>
    <div class="sponsor c-ink"><i class="round" style="background:#555"></i>Inkwell Printing</div>
    <div class="sponsor c-red">Pinecrest Roadlines</div>
    <div class="sponsor"></div>
  </section>

  <div class="register">
    <p class="register-title">FOR REGISTRATION CONTACT:</p>
    <p class="register-phones">0409318827 / 0408261395</p>
    <p class="register-close">Registrations Closing: 18th March</p>
  </div>
</main>
</body>
</html>
```